Harbor Compass - Book Cover

I need a book cover for my debut work, "Harbor Compass - Turning the Tide, One Step at a Time." While the website isn't complete, you can get a sense of what I am writing about by looking at my website, harborcompassbooks.org. The book is a leadership development book, but more of a personal change journey. The emphasis is on figuring out how to combine you work, social, and own self into an authentic package that not only resonates with others, but makes what you achieve more fulfilling.

I am attaching a copy of my logo so you can get a sense of what I like. I would prefer to not have the cover be photographic, but am open to suggestions. This will be a series of books so maintaining some sense of style will be important, and can garner future work.

Industry/Entity Type

Leadership

```html
<!DOCTYPE html>
<html lang="en">
<head>
<meta charset="utf-8">
<title>Harbor Compass – Book Cover</title>
<link rel="stylesheet" href="https://fonts.googleapis.com/css2?family=Open+Sans:ital,wght@0,400;0,600;0,700;1,600;1,700&display=swap">
<style>
  :root {
    --blue: #2f6db5;
    --paper: #efefef;
    --ink: #111111;
    --grey: #6b6b6d;
    --white: #ffffff;
    --spine: #ffffff;
  }
  * { margin: 0; padding: 0; box-sizing: border-box; }
  html, body { width: 1200px; height: 880px; overflow: hidden; background: var(--white); }
  body { font-family: "Open Sans", Arial, sans-serif; color: var(--ink); }

  .cover { position: relative; width: 1200px; height: 880px; }

  .panel { position: absolute; top: 0; height: 880px; background: var(--paper); overflow: hidden; }
  .panel--back { left: 0; width: 570px; }
  .panel--front { left: 623px; width: 577px; }
  .panel__band { position: absolute; left: 0; right: 0; background: var(--blue); }
  .panel__band--top { top: 0; height: 87px; }
  .panel__band--lower { top: 618px; height: 170px; }

  .spine { position: absolute; left: 570px; top: 0; width: 53px; height: 880px; background: var(--spine); }
  .spine__title {
    position: absolute; top: 94px; left: 50%; transform: translateX(-50%);
    writing-mode: vertical-rl; font-size: 16.5px; font-weight: 600; white-space: nowrap;
  }
  .spine__imprint {
    position: absolute; top: 626px; left: 50%; transform: translateX(-50%);
    writing-mode: vertical-rl; font-size: 14px; font-weight: 600; color: var(--blue); white-space: nowrap;
  }
  .spine__mark { position: absolute; top: 754px; left: 19px; }

  .series-name { text-align: center; font-weight: 400; }
  .series-name__lead { color: var(--blue); }
  .series-name__tail { color: var(--grey); }
  .rule { position: absolute; height: 2px; background: var(--ink); }

  /* back */
  .back__series { position: absolute; top: 146px; left: 0; width: 570px; font-size: 30px; }
  .back__title { position: absolute; top: 198px; left: 0; width: 570px; text-align: center; font-size: 25px; font-weight: 600; }
  .back__rule { top: 252px; left: 72px; width: 433px; }
  .back__pull {
    position: absolute; top: 275px; left: 110px; width: 350px; text-align: center;
    font-size: 13.5px; font-weight: 600; font-style: italic; line-height: 17px;
  }
  .back__blurb {
    position: absolute; top: 383px; left: 44px; width: 496px; text-align: center;
    font-size: 12.4px; font-weight: 600; line-height: 17px;
  }
  .back__contact { position: absolute; left: 76px; color: var(--white); font-size: 13.5px; }
  .back__contact--details { top: 677px; }
  .back__contact--post { top: 710px; }
  .back__imprint { position: absolute; top: 812px; left: 145px; display: flex; align-items: center; gap: 16px; }
  .back__imprint-name { font-size: 29px; color: var(--blue); }

  /* front */
  .front__series { position: absolute; top: 145px; left: 0; width: 577px; font-size: 45px; font-weight: 600; }
  .front__rule--top { top: 216px; left: 83px; width: 432px; }
  .front__title { position: absolute; top: 252px; left: 0; width: 577px; text-align: center; font-size: 58px; font-weight: 600; line-height: 76px; }
  .front__title-line { display: block; }
  .front__title-line--accent { color: var(--blue); }
  .front__title-line--muted { color: var(--grey); }
  .front__rule--bottom { top: 587px; left: 83px; width: 432px; }
  .front__quote {
    position: absolute; top: 680px; left: 78px; width: 425px; text-align: center;
    color: var(--white); font-size: 13.5px; font-weight: 600; line-height: 17px;
  }
  .front__author { position: absolute; top: 810px; left: 0; width: 577px; text-align: center; font-size: 28px; font-weight: 600; }
</style>
</head>
<body>
<main class="cover">

  <section class="panel panel--back" aria-label="Back cover">
    <div class="panel__band panel__band--top"></div>
    <h2 class="series-name back__series"><span class="series-name__lead">Harbor</span> <span class="series-name__tail">Compass</span></h2>
    <p class="back__title">Turning The Tide One Step at a Time</p>
    <div class="rule back__rule"></div>
    <p class="back__pull">“Positive endorsement or enticing description about your book goes here. The wording should be no more than three lines ”</p>
    <p class="back__blurb">“Lorem Ipsum is simply dummy text of the printing and typesetting industry. Lorem Ipsum has been the industry's standard dummy text ever since the 1500s, when an unknown printer took a galley of type and scrambled it to make a type specimen book. It has survived not only five centuries, but also the leap into electronic typesetting, remaining essentially unchanged. It was popularised in the 1960s with the release of Transfertype sheets containing Lorem Ipsum passages, and more recently with desktop publishing software like Quillset Composer including versions of Lorem Ipsum.”</p>
    <div class="panel__band panel__band--lower"></div>
    <p class="back__contact back__contact--details">Contact details</p>
    <p class="back__contact back__contact--post">post adress</p>
    <div class="back__imprint">
      <svg width="40" height="40" viewBox="0 0 40 40" aria-hidden="true"><circle cx="20" cy="20" r="19" fill="var(--blue)"/></svg>
      <span class="back__imprint-name">Harbor Compass</span>
    </div>
  </section>

  <section class="spine" aria-label="Spine">
    <span class="spine__title">Turning The Tide One Step at a Time</span>
    <span class="spine__imprint">Harbor Compass</span>
    <svg class="spine__mark" width="16" height="16" viewBox="0 0 16 16" aria-hidden="true"><circle cx="8" cy="8" r="7.5" fill="var(--blue)"/></svg>
  </section>

  <section class="panel panel--front" aria-label="Front cover">
    <div class="panel__band panel__band--top"></div>
    <h2 class="series-name front__series"><span class="series-name__lead">Harbor</span> <span class="series-name__tail">Compass</span></h2>
    <div class="rule front__rule--top"></div>
    <h1 class="front__title">
      <span class="front__title-line">Turning</span>
      <span class="front__title-line front__title-line--accent">The Tide,</span>
      <span class="front__title-line">One Step at a</span>
      <span class="front__title-line front__title-line--muted">Time</span>
    </h1>
    <div class="rule front__rule--bottom"></div>
    <div class="panel__band panel__band--lower"></div>
    <p class="front__quote">“A three line quote from the book, description of the subject or positive endorsement from a reviewer. Use ten to twelve point size typeface”</p>
    <p class="front__author">Author Name Here</p>
  </section>

</main>
</body>
</html>
```